Fashion Design Business Card

I need a new business card designed for a new fashion company. I have attached what I have currently designed. I want it more feminine looking, the logo needs to be gold. I want it simple, feminine and stylish. Please give me some different ideas with the fonts.

I need to send the design we currently have, as we have worked out the logo.
You also need all of our details
Fashion

```html
<!DOCTYPE html>
<html lang="en">
<head>
<meta charset="utf-8">
<title>Mirela Hastings – Business Card</title>
<link rel="stylesheet" href="https://fonts.googleapis.com/css2?family=Bodoni+Moda:wght@500;600&family=Arimo&display=swap">
<style>
  :root {
    --page: #ffffff;
    --ink: #111111;
    --card-black: #000000;
    --card-charcoal: #141414;
    --gold: #c9a650;
    --gold-light: #e6cf8a;
    --gold-deep: #7a5e1c;
  }
  * { margin: 0; padding: 0; box-sizing: border-box; }
  html, body { width: 1200px; height: 387px; overflow: hidden; background: var(--page); }
  .sheet { position: relative; width: 1200px; height: 387px; }

  .side-label {
    position: absolute; top: 4px; width: 200px; text-align: center;
    font-family: "Arimo", Arial, sans-serif; font-size: 22px; color: var(--ink);
  }
  .side-label--front { left: 202px; }
  .side-label--back { left: 790px; }

  .card { position: absolute; top: 52px; height: 328px; overflow: hidden; }
  .card--front {
    left: 16px; width: 574px;
    background: radial-gradient(ellipse at 50% 45%, #262626 0%, #0b0b0b 55%, var(--card-black) 100%);
  }
  .card--back { left: 610px; width: 580px; background: var(--card-charcoal); }

  .brand-name {
    font-family: "Bodoni Moda", "Times New Roman", serif;
    font-weight: 600; color: var(--gold);
    text-transform: uppercase; white-space: nowrap; line-height: 1.2;
  }

  .card--front .brand-name {
    position: absolute; left: 0; right: 0; top: 133px; text-align: center;
    font-size: 42px; letter-spacing: 2.5px;
  }

  .back-header {
    position: absolute; left: 0; top: 0; width: 100%; height: 62px; background: var(--card-black);
  }
  .back-header .brand-name {
    position: absolute; left: 8px; top: 1px; font-size: 50px; letter-spacing: 5px;
  }

  .title-tab {
    position: absolute; left: 0; top: 78px; width: 70px; height: 54px;
    background: linear-gradient(90deg, var(--gold-deep), var(--gold) 45%, rgba(20,20,20,0) 100%);
  }
  .role {
    position: absolute; left: 70px; top: 88px;
    font-family: "Bodoni Moda", "Times New Roman", serif; font-weight: 500;
    font-size: 28px; letter-spacing: 2px; color: var(--gold-light);
  }
  .contact-list { position: absolute; left: 18px; top: 156px; list-style: none; }
  .contact-list li {
    font-family: "Bodoni Moda", "Times New Roman", serif; font-weight: 500;
    font-size: 17px; letter-spacing: 1.5px; color: var(--gold); line-height: 31px;
  }
</style>
</head>
<body>
<main class="sheet">
  <p class="side-label side-label--front">front</p>
  <p class="side-label side-label--back">back</p>

  <section class="card card--front" aria-label="Card front">
    <h1 class="brand-name">Mirela Hastings</h1>
  </section>

  <section class="card card--back" aria-label="Card back">
    <header class="back-header">
      <p class="brand-name">Mirela Hastings</p>
    </header>
    <div class="title-tab"></div>
    <p class="role">Fashion Designer</p>
    <ul class="contact-list">
      <li>ph. 0400 213 648</li>
      <li>web: www.mirelahastings.com</li>
      <li>e.mail: mirela@mirelahastings.com</li>
    </ul>
  </section>
</main>
</body>
</html>
```